Marwick Estate Services (Handyman / Home Improvement Company)

Looking for a double sided professional looking business card with Logo attached to be highlighted on one side and throwing in an image of a handyman as an option would be nice to see as well. We are a company focused on providing quality Handyman and Home improvement services in a timely manner that is done right the first time with integrity

Industry/Entity Type

Handyman / Home Improvement

Contact Information for Business Card

(LOGO, Name, Mobile and office phone numbers, email) on front side of card, (the words "The SOLUTION to all of your Handyman and Home Improvement needs" followed by "Family Owned and Operated" at the very bottom) on the back.

Colors
EB3D1F
EC4F4E
F09395
F8D3D4
FCEDEE

Requirements
Must have
• Red, Gray, Black Color scheme
Should not have
• No Yellow or Blue colors

```html
<!DOCTYPE html>
<html lang="en">
<head>
<meta charset="utf-8">
<title>Marwick Estate Services – Business Card</title>
<link href="https://fonts.googleapis.com/css2?family=Montserrat:wght@700;800&family=Roboto:wght@300;400&display=swap" rel="stylesheet">
<style>
  :root {
    --backdrop: #262626;
    --card-black: #121212;
    --tone-1: #7a7a7a;
    --tone-2: #646464;
    --tone-3: #4f4f4f;
    --tone-4: #3d3d3d;
    --tone-5: #2f2f2f;
    --card-white: #ffffff;
    --ink: #111111;
    --gray: #555555;
    --gray-light: #8a8a8a;
    --divider: #9aa0a6;
    --red: #eb3d1f;
  }
  * { box-sizing: border-box; margin: 0; padding: 0; }
  html, body { width: 1200px; height: 900px; overflow: hidden; }
  body {
    background: var(--backdrop);
    font-family: "Roboto", Arial, sans-serif;
    display: flex;
    flex-direction: column;
    align-items: center;
    justify-content: center;
    gap: 40px;
  }
  .card {
    width: 640px;
    height: 366px;
    position: relative;
    overflow: hidden;
    border-radius: 3px;
  }

  /* Pattern side */
  .card-pattern {
    background: var(--card-black);
    padding: 18px 0 0 0;
  }
  .pattern-row {
    display: flex;
    height: 66px;
    align-items: center;
    margin-left: 10px;
  }
  .pattern-row.is-offset { margin-left: 60px; }
  .pattern-item {
    flex: none;
    width: 100px;
    text-align: center;
    font-family: "Montserrat", Arial, sans-serif;
    font-weight: 800;
    font-size: 10px;
    line-height: 1.2;
    letter-spacing: 0.4px;
    text-transform: uppercase;
  }
  .tone-1 { color: var(--tone-1); }
  .tone-2 { color: var(--tone-2); }
  .tone-3 { color: var(--tone-3); }
  .tone-4 { color: var(--tone-4); }
  .tone-5 { color: var(--tone-5); }
  .pattern-item.is-highlight { color: var(--red); }

  /* Contact side */
  .card-contact { background: var(--card-white); }
  .brand {
    position: absolute;
    left: 40px;
    top: 118px;
    width: 230px;
    display: flex;
    align-items: center;
    gap: 10px;
  }
  .brand .mark-square {
    flex: none;
    width: 18px; height: 18px; background: var(--red);
  }
  .brand-name {
    font-family: "Montserrat", Arial, sans-serif;
    font-weight: 800;
    font-size: 26px;
    line-height: 1.1;
    color: var(--red);
    text-transform: uppercase;
  }
  .divider {
    position: absolute;
    left: 300px;
    top: 62px;
    width: 1px;
    height: 180px;
    background: var(--divider);
  }
  .details {
    position: absolute;
    left: 322px;
    top: 62px;
  }
  .person-name {
    font-family: "Montserrat", Arial, sans-serif;
    font-weight: 800;
    font-size: 17px;
    color: var(--ink);
    letter-spacing: 0.3px;
  }
  .person-title {
    font-size: 13px;
    color: var(--red);
    margin-top: 1px;
  }
  .address {
    margin-top: 12px;
    font-size: 14px;
    line-height: 1.3;
    color: var(--gray);
  }
  .contact-list {
    list-style: none;
    margin-top: 12px;
  }
  .contact-list li {
    display: flex;
    align-items: center;
    gap: 9px;
    font-size: 14px;
    line-height: 1.4;
    color: var(--gray);
  }
  .contact-list svg { width: 13px; height: 13px; flex: none; }
  .tagline {
    position: absolute;
    left: 0; right: 0;
    bottom: 40px;
    text-align: center;
    font-size: 14px;
    font-weight: 300;
    line-height: 1.4;
    color: var(--gray-light);
  }
</style>
</head>
<body>

  <section class="card card-pattern" aria-label="Card side with repeated company name pattern">
    <div class="pattern-row">
      <span class="pattern-item tone-1">Marwick<br>Estate Services</span>
      <span class="pattern-item tone-1">Marwick<br>Estate Services</span>
      <span class="pattern-item tone-2">Marwick<br>Estate Services</span>
      <span class="pattern-item tone-2">Marwick<br>Estate Services</span>
      <span class="pattern-item tone-3">Marwick<br>Estate Services</span>
      <span class="pattern-item tone-3">Marwick<br>Estate Services</span>
    </div>
    <div class="pattern-row is-offset">
      <span class="pattern-item tone-1">Marwick<br>Estate Services</span>
      <span class="pattern-item tone-2">Marwick<br>Estate Services</span>
      <span class="pattern-item tone-2">Marwick<br>Estate Services</span>
      <span class="pattern-item tone-3">Marwick<br>Estate Services</span>
      <span class="pattern-item is-highlight">Marwick<br>Estate Services</span>
      <span class="pattern-item tone-4">Marwick<br>Estate Services</span>
    </div>
    <div class="pattern-row">
      <span class="pattern-item tone-2">Marwick<br>Estate Services</span>
      <span class="pattern-item tone-2">Marwick<br>Estate Services</span>
      <span class="pattern-item tone-3">Marwick<br>Estate Services</span>
      <span class="pattern-item tone-3">Marwick<br>Estate Services</span>
      <span class="pattern-item tone-4">Marwick<br>Estate Services</span>
      <span class="pattern-item tone-4">Marwick<br>Estate Services</span>
    </div>
    <div class="pattern-row is-offset">
      <span class="pattern-item tone-2">Marwick<br>Estate Services</span>
      <span class="pattern-item tone-3">Marwick<br>Estate Services</span>
      <span class="pattern-item tone-3">Marwick<br>Estate Services</span>
      <span class="pattern-item tone-4">Marwick<br>Estate Services</span>
      <span class="pattern-item tone-4">Marwick<br>Estate Services</span>
      <span class="pattern-item tone-5">Marwick<br>Estate Services</span>
    </div>
    <div class="pattern-row">
      <span class="pattern-item tone-3">Marwick<br>Estate Services</span>
      <span class="pattern-item tone-3">Marwick<br>Estate Services</span>
      <span class="pattern-item tone-4">Marwick<br>Estate Services</span>
      <span class="pattern-item tone-4">Marwick<br>Estate Services</span>
      <span class="pattern-item tone-5">Marwick<br>Estate Services</span>
      <span class="pattern-item tone-5">Marwick<br>Estate Services</span>
    </div>
  </section>

  <section class="card card-contact" aria-label="Card side with contact details">
    <div class="brand">
      <span class="mark-square"></span>
      <span class="brand-name">Marwick Estate Services</span>
    </div>

    <div class="divider"></div>

    <div class="details">
      <h1 class="person-name">DORIAN VELL</h1>
      <p class="person-title">Managing Director</p>
      <p class="address">Alder Row Unit 7<br>Fenwick, CA 90210</p>
      <ul class="contact-list">
        <li>
          <svg viewBox="0 0 16 16" aria-hidden="true"><path fill="#eb3d1f" d="M3.6 1.5l2.2 2.6-1.2 1.7c.9 2 2.4 3.5 4.4 4.4l1.7-1.2 2.6 2.2-1.3 2.3C6.8 13.5 2.5 9.2 1.3 3z"/></svg>
          555.014.2210
        </li>
        <li>
          <svg viewBox="0 0 16 16" aria-hidden="true"><rect x="4" y="1" width="8" height="14" rx="1.5" fill="none" stroke="#eb3d1f" stroke-width="1.6"/><circle cx="8" cy="12.5" r="0.9" fill="#eb3d1f"/></svg>
          555.017.3348
        </li>
        <li>
          <svg viewBox="0 0 16 16" aria-hidden="true"><rect x="1" y="3" width="14" height="10" rx="1" fill="#eb3d1f"/><path d="M1.5 3.8L8 9l6.5-5.2" fill="none" stroke="#fff" stroke-width="1.3"/></svg>
          dorian@marwickestate.com
        </li>
        <li>
          <svg viewBox="0 0 16 16" aria-hidden="true"><circle cx="8" cy="8" r="7" fill="#eb3d1f"/><path d="M1 8h14M8 1c-2.5 2.5-2.5 11.5 0 14M8 1c2.5 2.5 2.5 11.5 0 14" fill="none" stroke="#fff" stroke-width="1"/></svg>
          www.marwickestate.com
        </li>
      </ul>
    </div>

    <p class="tagline">Your SOLUTION to all of your Handyman and Home Improvement needs"<br>followed by "Family Owned and Operated"</p>
  </section>

</body>
</html>
```